Game, Voice & Dedicated Server Company Needs a Business Card Design

We need a new business card design, centered around our new logo (PSD provided below).

Designs that we do like:
https://pixelmarsh.net/item/corporate-business-card/5382017?s_rank=43 (needs to be made more eye catching)

Our main areas of business are:
- Dedicated Servers
- Game Servers
- Voice Servers
- Mitigation Security Specialists

Industry/Entity Type

Business

Contact Information for Business Card

On the card: (and anything else you would suggest)
- Staff member name
- Staff member position in company
- Staff member phone number
- Staff member email
- Other / Staff member Skype
- Website link

Colors
9bcb3c
abd036

Requirements
Must have
• Design of Card:
• - Green (same green as the logo)
• - Business / Corporate design
• - Something a little different / abstract that shouts premium

```html
<!DOCTYPE html>
<html lang="en">
<head>
<meta charset="utf-8">
<title>Corvane Servers – Business Card</title>
<link rel="stylesheet" href="https://fonts.googleapis.com/css2?family=Open+Sans:ital,wght@0,400;0,600;0,700;1,400&display=swap">
<style>
  :root {
    --stage: #e9e9e6;
    --green: #8cc63f;
    --black: #111213;
    --black-soft: #222325;
    --grey-light: #d4d5d7;
    --grey-mid: #a4a5a8;
    --grey-dark: #55575a;
    --white: #ffffff;
    --ink: #1d1e1f;
  }
  * { box-sizing: border-box; margin: 0; padding: 0; }
  html, body {
    width: 1200px; height: 950px; overflow: hidden;
    background: var(--stage);
    font-family: "Open Sans", Arial, sans-serif;
  }
  .sheet {
    width: 1200px; height: 950px;
    display: flex; flex-direction: column; align-items: center; justify-content: center;
    gap: 26px;
  }
  .card {
    position: relative;
    width: 760px; height: 434px;
    overflow: hidden;
    box-shadow: 0 6px 18px rgba(0,0,0,.18);
  }

  /* front */
  .card-front { background: linear-gradient(160deg, var(--black-soft), var(--black) 60%); }
  .front-band { position: absolute; inset: 0; width: 100%; height: 100%; }
  .holder {
    position: absolute; top: 36px; right: 48px;
    text-align: right; color: var(--ink);
  }
  .holder-name { font-size: 22px; font-weight: 600; letter-spacing: .3px; line-height: 1.2; }
  .holder-role { font-size: 13px; margin-top: 2px; }

  .online {
    position: absolute; top: 176px; right: 40px;
    list-style: none; text-align: right;
  }
  .online li {
    display: flex; align-items: center; justify-content: flex-end; gap: 10px;
    color: var(--white); font-size: 15px; line-height: 30px;
  }

  .brand {
    position: absolute; left: 60px; top: 262px;
    display: flex; align-items: center; gap: 14px;
  }
  .brand-square { width: 22px; height: 22px; background: var(--green); }
  .brand-name {
    color: var(--green); font-weight: 700; font-size: 30px; line-height: 1.0;
    letter-spacing: .5px; text-transform: uppercase;
  }

  .direct {
    position: absolute; left: 60px; top: 348px; list-style: none;
  }
  .direct li {
    display: flex; align-items: center; gap: 10px;
    color: var(--white); font-size: 15px; line-height: 28px;
  }
  .icon { width: 14px; height: 14px; flex: none; }

  /* back */
  .card-back { background: var(--green); }
  .back-brand {
    position: absolute; left: 360px; top: 150px;
    display: flex; align-items: center; gap: 18px;
  }
  .back-brand .brand-square { width: 34px; height: 34px; background: var(--grey-dark); }
  .back-brand .brand-name { color: var(--grey-dark); font-size: 52px; }

  .services {
    position: absolute; left: 40px; bottom: 36px;
    list-style: none; display: flex; gap: 14px;
    font-size: 15px; font-style: italic; color: var(--ink);
  }
  .services li::before { content: "•"; margin-right: 12px; font-style: normal; }
  .services li:first-child::before { content: none; }
</style>
</head>
<body>
<main class="sheet">

  <section class="card card-front" aria-label="Card front">
    <svg class="front-band" viewBox="0 0 760 434" preserveAspectRatio="none" aria-hidden="true">
      <defs>
        <linearGradient id="band-grey" x1="0" y1="0" x2="0" y2="1">
          <stop offset="0" stop-color="#d9dadc"/>
          <stop offset="1" stop-color="#98999c"/>
        </linearGradient>
      </defs>
      <polygon points="0,0 760,0 760,128 0,232" fill="url(#band-grey)"/>
      <polygon points="0,232 760,128 760,136 0,240" fill="#000000" opacity=".25"/>
    </svg>

    <div class="holder">
      <p class="holder-name">Daniel Reyes</p>
      <p class="holder-role">CEO/Founder</p>
    </div>

    <ul class="online">
      <li>name@corvane.com
        <svg class="icon" viewBox="0 0 14 14"><rect width="14" height="14" rx="2" fill="var(--green)"/><path d="M3 4.5h8v5H3z M3 4.5l4 3 4-3" fill="none" stroke="#111" stroke-width="1.1"/></svg>
      </li>
      <li>www.corvane.com
        <svg class="icon" viewBox="0 0 14 14"><circle cx="7" cy="7" r="7" fill="var(--green)"/><circle cx="7" cy="7" r="3.6" fill="none" stroke="#111" stroke-width="1.1"/><path d="M3.4 7h7.2" stroke="#111" stroke-width="1.1"/></svg>
      </li>
    </ul>

    <div class="brand">
      <span class="brand-square" aria-hidden="true"></span>
      <p class="brand-name">Corvane<br>Servers</p>
    </div>

    <ul class="direct">
      <li>
        <svg class="icon" viewBox="0 0 14 14"><path d="M3.2 1.5l2.2 2.6-1.2 1.6c.8 1.8 2.2 3.2 4 4l1.6-1.2 2.6 2.2-1.4 2c-5 .2-9.5-4.3-9.3-9.3z" fill="var(--green)"/></svg>
        555 014 2538
      </li>
      <li>
        <svg class="icon" viewBox="0 0 14 14"><circle cx="7" cy="7" r="7" fill="var(--green)"/></svg>
        corvane.com
      </li>
    </ul>
  </section>

  <section class="card card-back" aria-label="Card back">
    <div class="back-brand">
      <span class="brand-square" aria-hidden="true"></span>
      <p class="brand-name">Corvane</p>
    </div>
    <ul class="services">
      <li>Dedicated Servers</li>
      <li>Game Servers</li>
      <li>Voice Servers</li>
      <li>Business relations</li>
    </ul>
  </section>

</main>
</body>
</html>
```